Brennock Holdings LLC, new Business cards

I'm moving offices and need new cards. Plus I'm open to modifying the current design of my card. I will keep the logo but would like to explore other layouts and fonts for the design. I've included the current double sided card for reference. I Like the navy color and white. Might be open to grays or silver. Needs to be clean and elegant.

Target Market(s)

Investors, buyers & sellers of private equities and real estate.

Contact Information for Business Card

Brennock Holdings
Desmond K.R. Whitfield, Managing Principal
418 Harwick Ave., Suite 310
Denver, CO 80299
M: 970-555-0147, O: 303-555-0193
Desmond@brennockholdings.example
Brennockholdings.example

Colors
0354a2
ffffff
c4c4c4

Requirements
Must have
• Business card details.
• Logo raised or embossed, it was designed after a wax seal. Current has raised ink.
Nice to have
• Space on card to write additional notes.

```html
<!DOCTYPE html>
<html lang="en">
<head>
<meta charset="utf-8">
<title>Brennock Holdings – Business Card</title>
<link rel="stylesheet" href="https://fonts.googleapis.com/css2?family=Lato:wght@400;700&display=swap">
<style>
  :root {
    --navy: #25234f;
    --white: #ffffff;
    --silver-light: #e6e6e6;
    --silver-mid: #c4c4c4;
    --silver-dark: #9a9a9a;
    --rule: #8a89a3;
    --backdrop: #eeeeee;
  }
  html, body {
    margin: 0;
    width: 1200px;
    height: 1108px;
    overflow: hidden;
    background: var(--backdrop);
    font-family: "Lato", sans-serif;
  }
  .stage {
    position: relative;
    width: 1200px;
    height: 1108px;
  }
  .card {
    position: absolute;
    top: 234px;
    width: 380px;
    height: 640px;
    border-radius: 24px;
    box-shadow: 0 6px 18px rgba(0,0,0,0.18);
    overflow: hidden;
  }
  .card--front {
    left: 190px;
    background: var(--white);
    color: var(--navy);
  }
  .card--back {
    left: 630px;
    background: linear-gradient(180deg, var(--silver-light) 0%, #f4f4f4 22%, var(--silver-mid) 60%, var(--silver-dark) 100%);
  }
  .brand {
    position: absolute;
    top: 56px;
    left: 0;
    right: 0;
    text-align: center;
  }
  .brand__dot {
    display: block;
    margin: 0 auto 14px;
    width: 140px;
    height: 140px;
    border-radius: 50%;
    background: var(--navy);
  }
  .brand__name {
    font-size: 19px;
    font-weight: 700;
    letter-spacing: 2px;
    text-transform: uppercase;
    color: var(--navy);
  }
  .details {
    position: absolute;
    top: 300px;
    left: 40px;
    right: 30px;
    font-size: 16px;
    line-height: 1.35;
  }
  .details p {
    margin: 0;
    white-space: nowrap;
  }
  .details__name {
    font-size: 21px;
    font-weight: 700;
    letter-spacing: 0.5px;
    text-transform: uppercase;
    margin: 0;
    white-space: nowrap;
  }
  .details__title,
  .details__address p {
    padding-left: 30px;
  }
  .rule {
    border: 0;
    border-top: 1px solid var(--rule);
    margin: 10px 0 10px 30px;
    width: 200px;
  }
  .details__contact { font-size: 15px; }
  .label { font-weight: 700; }
  .web { font-weight: 700; }
</style>
</head>
<body>
<div class="stage">
  <section class="card card--front">
    <div class="brand">
      <span class="brand__dot"></span>
      <span class="brand__name">Brennock Holdings</span>
    </div>
    <div class="details">
      <h1 class="details__name">Desmond K.R. Whitfield</h1>
      <p class="details__title">Managing Principal</p>
      <hr class="rule">
      <div class="details__address">
        <p>418 Harwick Ave., Suite 310</p>
        <p>Denver, CO 80299</p>
      </div>
      <hr class="rule">
      <div class="details__contact">
        <p><span class="label">P:</span> 970-555-0147 | <span class="label">O:</span> 303-555-0193</p>
        <p><span class="label">E:</span> Desmond@brennockholdings.example</p>
        <p class="web">www.Brennockholdings.example</p>
      </div>
    </div>
  </section>
  <section class="card card--back" role="img" aria-label="Silver back of the card with a repeating embossed seal pattern"></section>
</div>
</body>
</html>
```